Rebuild

Hello,
I got a new logo, and a new business name. Now I need that new identity on a new web page.
Please take a look at my existing site. www.critterfixhub.com
and please build me a new website with my new logo and get it posted at my new domain www.tomvarlowcapture.com
Updates
Please include in the design the Radio marketing tagline "Tom Varlow, Raised and Ready for Wildlife Control".
I would like to add that it is usually understood that I will capture and remove problem causing animals. However, what I really need to emphasize is that I fortify homes and other structures to keep the animals out long term. Trapping is a temporary solution. Home fortification such as reinforcing vent screens, sealing holes, and constructing secure barriers is the Permanent solution. Kind of like a home security system for vertebrate pests. You don't really need an alarm system if you have the best locks and steel doors.
Obviously, my website is a multiple page website. Some designs will be good for the home page, and others for secondary pages.
Ultimately, I need a good home page that will attract clients, and then good backup pages to explain the different aspects of my work.
I imagine a home page. Sub pages would include Home Fortifications, Species detail pages, Company history, FAQs, Odd and unusual services, specialties, and where to go for the things I don't do. The text for these pages is something I can write myself. I'm a good writer. Just not a very good visual artist.
I have added the logo in .eps, and I have also added the mirror image logo in both eps and jpg. Let me know if other formats are needed.
I've posted a bunch of photos on my facebook for perusal
http://www.facebook.com/pages/Tom-Varlow-Wildlife-Control/902315748160334
Target Market(s)
Upper to middle income homeowners
Industry/Entity Type
Business
Look and feel
Each slider illustrates characteristics of the customer's brand and the style your logo design should communicate.

```html
<!DOCTYPE html>
<html lang="en">
<head>
<meta charset="utf-8">
<title>Tom Varlow Wildlife Control</title>
<link rel="stylesheet" href="https://fonts.googleapis.com/css2?family=Arimo:ital,wght@0,400;0,700;1,400&family=Roboto+Condensed:wght@700&display=swap">
<style>
  :root {
    --ink: #1d1b16;
    --white: #ffffff;
    --grey-text: #9a9a9a;
    --grey-more: #4a4a4a;
    --nav-bg: #252525;
    --nav-line: #3c3c3c;
    --yellow: #f5bf0f;
    --yellow-bright: #fcc80d;
    --yellow-deep: #d8a80d;
    --footer-text: #8c8c8c;
    --dot: #dedede;
  }
  * { box-sizing: border-box; margin: 0; padding: 0; }
  html, body { width: 1200px; height: 1055px; overflow: hidden; background: var(--white); }
  body { font-family: "Arimo", Arial, sans-serif; color: var(--ink); }
  .page { position: relative; width: 1200px; height: 1055px; }

  .brand { position: absolute; left: 152px; top: 56px; display: flex; align-items: center; gap: 12px; }
  .brand-mark { width: 30px; height: 30px; border-radius: 50%; background: var(--yellow); }
  .brand-name { font-size: 30px; font-weight: 700; color: var(--ink); }

  .contact { position: absolute; right: 96px; top: 16px; text-align: right; }
  .contact-phone { display: flex; align-items: center; justify-content: flex-end; gap: 6px; font-size: 36px; font-weight: 700; }
  .contact-address { font-size: 16.5px; font-weight: 700; line-height: 26px; margin-top: 2px; }

  .main-nav { position: absolute; left: 47px; top: 164px; width: 1101px; height: 47px; background: var(--nav-bg); display: flex; }
  .main-nav a { display: flex; align-items: center; justify-content: center; color: var(--white); text-decoration: none; font-size: 15px; border-right: 1px solid var(--nav-line); }
  .main-nav a:last-child { border-right: 0; }
  .main-nav a.current { color: var(--yellow); }

  .hero-kicker { position: absolute; left: 90px; top: 257px; font-size: 23px; font-style: italic; color: var(--grey-text); }
  .hero-title { position: absolute; left: 89px; top: 303px; font-size: 48px; line-height: 1; font-weight: 700; color: var(--grey-text); letter-spacing: -0.8px; white-space: nowrap; }
  .hero-title span { color: var(--yellow); }
  .hero-sub { position: absolute; left: 90px; top: 359px; font-size: 18px; font-style: italic; color: var(--grey-text); }
  .more { font-family: "Roboto Condensed", "Arial Narrow", sans-serif; font-weight: 700; font-size: 29px; color: var(--grey-more); text-decoration: none; letter-spacing: 0.5px; }
  .more small { font-family: "Arimo", Arial, sans-serif; font-size: 15px; margin-left: 6px; vertical-align: 6px; }
  .hero-more { position: absolute; left: 93px; top: 412px; }
  .slider-dots { position: absolute; left: 94px; top: 488px; display: flex; gap: 7px; }
  .slider-dots i { width: 23px; height: 23px; border-radius: 50%; background: var(--dot); }
  .slider-dots i.active { background: radial-gradient(circle at 40% 35%, #ffe45a, #e3aa00); }

  .hero-photo { position: absolute; left: 600px; top: 234px; width: 513px; height: 393px; border-radius: 46% 40% 30% 30%; background: radial-gradient(ellipse at 45% 45%, #6c6a66 0%, #8e8b86 45%, #d7d5d1 80%, rgba(255,255,255,0) 100%); }

  .features { position: absolute; left: 416px; top: 641px; width: 732px; height: 350px; background: linear-gradient(90deg, #ecb90f, var(--yellow-deep)); }
  .feature-lead { position: absolute; left: 47px; top: 562px; width: 366px; height: 429px; background: linear-gradient(90deg, var(--yellow), var(--yellow-bright)); box-shadow: 5px 0 6px rgba(0,0,0,0.35); padding: 42px 0 0 44px; }
  .feature { position: absolute; }
  .feature h2 { font-size: 30px; font-weight: 700; letter-spacing: -0.3px; }
  .feature-lead h2 { font-size: 57px; letter-spacing: -0.5px; }
  .feature h3 { font-size: 16.5px; font-weight: 700; line-height: 27px; margin-top: 22px; }
  .feature-lead h3 { margin-top: 26px; }
  .feature p { font-size: 15px; line-height: 27px; margin-top: 10px; }
  .feature .more { position: absolute; color: #3a3016; }
  .feature-lead .more { left: 44px; top: 372px; }
  .feature-col { top: 683px; width: 300px; }
  .feature-col .more { left: 0; top: 252px; }
  .feature-col.one { left: 469px; }
  .feature-col.two { left: 812px; }

  .site-footer { position: absolute; left: 47px; top: 991px; width: 1101px; height: 38px; background: var(--nav-bg); border-top: 2px solid #111; color: var(--footer-text); font-size: 14px; padding: 10px 0 0 46px; }
</style>
</head>
<body>
<div class="page">
  <header>
    <div class="brand"><span class="brand-mark"></span><span class="brand-name">Tom Varlow</span></div>
    <div class="contact">
      <div class="contact-phone">
        <svg width="30" height="30" viewBox="0 0 24 24" aria-hidden="true"><path fill="#1d1b2a" d="M6.6 2.5c.8-.5 1.8-.3 2.3.5l1.6 2.6c.5.8.3 1.8-.4 2.3l-1.3 1c.8 2.1 2.2 4 4 5.3l1.2-1c.7-.6 1.8-.5 2.4.2l2 2.2c.6.7.6 1.8-.1 2.4l-1.4 1.3C12 19 5 12 5 4.3z"/></svg>
        <span>(415) 555-0187</span>
      </div>
      <div class="contact-address">1840 Harbor Lane, Suite 12<br>Oakdale, CA 95361</div>
    </div>
    <nav class="main-nav">
      <a class="current" href="#" style="width:131px">HOME</a>
      <a href="#" style="width:161px">ABOUT US</a>
      <a href="#" style="width:214px">ANIMAL CONTROL</a>
      <a href="#" style="width:226px">WILDLIFE SERVICES</a>
      <a href="#" style="width:190px">TESTIMONIALS</a>
      <a href="#" style="width:179px">CONTACT US</a>
    </nav>
  </header>

  <section class="hero">
    <div class="hero-kicker">TOM VARLOW</div>
    <h1 class="hero-title">RAISED <span>AND READY</span></h1>
    <div class="hero-sub">FOR WILDLIFE CONTROL</div>
    <a class="more hero-more" href="#">MORE<small>&gt;</small></a>
    <div class="slider-dots"><i></i><i class="active"></i><i></i><i></i><i></i></div>
    <div class="hero-photo" role="img" aria-label="Photo of a raccoon standing on a white background"></div>
  </section>

  <section>
    <div class="features"></div>
    <article class="feature feature-lead">
      <h2>AETERNO</h2>
      <h3>Ea prompta conceptam maiestatis<br>eum. Mei illud intellegam</h3>
      <p>Cu nec velit postea tincidunt, ei sea<br>electram dissentiet, vis at fugit putent<br>tritani. Ius ea quod accusamus<br>laboramus, sea id facilis probatus<br>forensibus. Eos an quis graece<br>salutatus, mea ex mutat libris quaeque.</p>
      <a class="more" href="#">MORE<small>&gt;</small></a>
    </article>
    <article class="feature feature-col one">
      <h2>NUSQUAM</h2>
      <h3>Ea prompta conceptam maiestatis<br>eum. Mei illud intellegam</h3>
      <p>Cu nec velit postea tincidunt, ei sea<br>electram dissentiet, vis at fugit putent<br>tritani. Ius ea quod accusamus laboramus,<br>sea id facilis probatus forensibus. Eos an</p>
      <a class="more" href="#">MORE<small>&gt;</small></a>
    </article>
    <article class="feature feature-col two">
      <h2>CONCEPT</h2>
      <h3>Ea prompta conceptam maiestatis<br>eum. Mei illud intellegam</h3>
      <p>Cu nec velit postea tincidunt, ei sea<br>electram dissentiet, vis at fugit putent<br>tritani. Ius ea quod accusamus laboramus,<br>sea id facilis probatus forensibus. Eos an</p>
      <a class="more" href="#">MORE<small>&gt;</small></a>
    </article>
  </section>

  <footer class="site-footer">Copyright © Tom Varlow Animal Control</footer>
</div>
</body>
</html>
```